Business card design needed

Double sided
Color, unique, elegant

Maybe put this quote somewhere?? But I think it might make it to cluttered?
“The Pilates Method of Body
Conditioning develops the body
uniformly, corrects posture, restores
vitality, invigorates the mind and
elevates the spirit”
- Henrik Dovacombe

Industry/Entity Type

Business

Contact Information for Business Card

Marta Kellbrook
Pilates Instructor & Personal trainer
Mobile: 0498265043
www.lorvix.com.au
email: lorvixhealth.fitness@qentamail.com

```html
<!DOCTYPE html>
<html lang="en">
<head>
<meta charset="utf-8">
<title>Lorvix Health &amp; Fitness – Business Card Back</title>
<link rel="stylesheet" href="https://fonts.googleapis.com/css2?family=Jost:ital,wght@0,300;1,300&display=swap">
<style>
  :root {
    --paper: #ffffff;
    --card-purple: #913f97;
    --ink-light: #ffffff;
  }
  html, body {
    margin: 0;
    padding: 0;
    width: 1200px;
    height: 693px;
    overflow: hidden;
    background: var(--paper);
  }
  .canvas {
    position: relative;
    width: 1200px;
    height: 693px;
    background: var(--paper);
  }
  .card-back {
    position: absolute;
    left: 48px;
    top: 47px;
    width: 1120px;
    height: 607px;
    background: var(--card-purple);
    color: var(--ink-light);
    font-family: "Jost", "Futura", sans-serif;
    font-weight: 300;
  }
  .contact-line {
    position: absolute;
    left: 0;
    right: 0;
    margin: 0;
    text-align: center;
    line-height: 1;
    white-space: nowrap;
  }
  .website {
    top: 212px;
    font-size: 38px;
    letter-spacing: 0.4em;
    padding-left: 0.4em;
  }
  .email {
    top: 265px;
    font-size: 34px;
    font-style: italic;
    letter-spacing: 0.22em;
    padding-left: 0.22em;
  }
  .phone {
    top: 358px;
    font-size: 45px;
    letter-spacing: 0.12em;
    padding-left: 0.12em;
  }
  .phone-dot {
    display: inline-block;
    font-size: 0.5em;
    vertical-align: 0.45em;
    margin: 0 0.1em;
  }
</style>
</head>
<body>
  <main class="canvas">
    <section class="card-back" aria-label="Contact details">
      <p class="contact-line website">www.lorvix.com.au</p>
      <p class="contact-line email">lorvixhealth.fitness@qentamail.com</p>
      <p class="contact-line phone">04<span class="phone-dot">•</span>9826<span class="phone-dot">•</span>5043</p>
    </section>
  </main>
</body>
</html>
```